New Business Card Design Project

Need a design that will create an impact / strong impression towards our clients for our business. We are in the lighting business and we do lighting retrofits for large commercial to industrial clientele.

Target Market(s)

Lighting Industry

Industry/Entity Type

Business

Other font styles liked:
• we would like to use the font on our logo, not sure what it is though..

Requirements
Must have
• Our logo.
Nice to have
• We are open to suggestions that have to do with lighting.

```html
<!DOCTYPE html>
<html lang="en">
<head>
<meta charset="utf-8">
<title>Brightline Retrofit Group – Business Card</title>
<link href="https://fonts.googleapis.com/css2?family=Open+Sans:wght@400;600;700&display=swap" rel="stylesheet">
<style>
  :root {
    --backdrop: #e6e4e1;
    --card: #ffffff;
    --green-dark: #1d4d24;
    --green-mid: #0f8542;
    --green-light: #6cbf5a;
    --text-grey: #666666;
    --photo-lilac: #d9c3e4;
    --photo-glow: #fbf3f8;
    --photo-warm: #f2d7c4;
  }
  * { box-sizing: border-box; margin: 0; padding: 0; }
  html, body { width: 1200px; height: 1000px; overflow: hidden; }
  body {
    background: var(--backdrop);
    font-family: "Open Sans", Arial, sans-serif;
    position: relative;
  }
  .card {
    position: absolute;
    left: 265px;
    width: 667px;
    height: 398px;
    background: var(--card);
    box-shadow: 0 4px 14px rgba(0,0,0,.18);
    overflow: hidden;
  }
  .card--front { top: 74px; }
  .card--back { top: 533px; }

  .brand {
    display: flex;
    align-items: center;
    gap: 10px;
    color: var(--green-dark);
    font-weight: 700;
    white-space: nowrap;
  }
  .brand__mark {
    width: 16px; height: 16px;
    background: var(--green-light);
  }
  .card--front .brand {
    position: absolute;
    top: 52px;
    right: 32px;
    font-size: 21px;
  }

  .holder { position: absolute; left: 34px; top: 160px; }
  .holder__name {
    color: var(--green-mid);
    font-size: 21px;
    font-weight: 700;
    letter-spacing: .3px;
    line-height: 1.2;
  }
  .holder__role { color: var(--text-grey); font-size: 16px; line-height: 1.3; }

  .address {
    position: absolute; left: 34px; top: 226px;
    color: var(--text-grey); font-size: 16px; line-height: 21px;
    font-style: normal;
  }
  .contacts {
    position: absolute; left: 34px; top: 278px;
    list-style: none;
    color: var(--text-grey); font-size: 16px; line-height: 24px;
  }
  .contacts li { display: flex; align-items: center; gap: 6px; }
  .contacts svg { width: 14px; height: 14px; fill: var(--green-mid); }

  .bands { position: absolute; left: 0; bottom: 0; width: 100%; height: 26px; display: flex; gap: 4px; }
  .bands span:nth-child(1) { width: 201px; background: var(--green-mid); }
  .bands span:nth-child(2) { width: 220px; background: var(--green-light); }
  .bands span:nth-child(3) { flex: 1; background: var(--green-dark); }

  .photo {
    position: absolute; inset: 0;
    background:
      radial-gradient(ellipse at 30% 75%, var(--photo-warm) 0%, transparent 45%),
      radial-gradient(ellipse at 55% 45%, var(--photo-glow) 0%, transparent 60%),
      linear-gradient(160deg, var(--photo-lilac) 0%, var(--photo-glow) 55%, var(--photo-lilac) 100%);
  }
  .card--back .brand {
    position: absolute;
    left: 0; right: 0; top: 168px;
    justify-content: center;
    font-size: 30px;
  }
  .card--back .brand__mark { width: 22px; height: 22px; }
  .tagline {
    position: absolute; left: 0; right: 0; top: 346px;
    text-align: center; color: #111; font-size: 15px;
  }
</style>
</head>
<body>
  <section class="card card--front">
    <div class="brand"><span class="brand__mark"></span>Brightline Retrofit Group, LLC</div>

    <div class="holder">
      <p class="holder__name">DANA WHITCOMBE</p>
      <p class="holder__role">Managing Director</p>
    </div>

    <address class="address">118 east 52nd street,<br>Harbor City, NY 10422</address>

    <ul class="contacts">
      <li><svg viewBox="0 0 14 14"><path d="M1 4c0-2 3-3 6-3s6 1 6 3v1h-3V3.5H4V5H1zM3 6h8l2 6H1z"/></svg>+ 555 014 2230</li>
      <li><svg viewBox="0 0 14 14"><path d="M1 3h12v8H1z M1 3l6 5 6-5" stroke="#fff" stroke-width="1"/></svg>info@brightlineretrofit.com</li>
      <li><svg viewBox="0 0 14 14"><circle cx="7" cy="7" r="6"/></svg>www.brightlineretrofit.com</li>
    </ul>

    <div class="bands"><span></span><span></span><span></span></div>
  </section>

  <section class="card card--back">
    <div class="photo" role="img" aria-label="Brightly lit industrial ceiling with steel trusses and glowing lights"></div>
    <div class="brand"><span class="brand__mark"></span>Brightline Retrofit Group, LLC</div>
    <p class="tagline">Large commercial to Industrial clientele</p>
  </section>
</body>
</html>
```